MARBLED SPARROW WEB DESIGN PROJECT

We are a brand new company called "Marbled Sparrow" which specialise in one-off Vintage Clothing. We would like somebody to design a web page which will be the sole income for our company. Our main aim is to have an easy searchable website which is user friendly. The key to the website is to target people who do not like the idea of op-shopping but love vintage clothes - this website will be the answer.
Updates

This website will need to be coded to work with Tin Lantern - Please read this before you start. https://help.tinlantern.example/articles/Public/How-do-I-create-custom-template-files-for-my-store

Hi everyone, Just want to make note that the this website is for young people. Just so people a clear I want modern young people dressed in Vintage clothes as this is that reality and what they would like to see. Not people dressed like they are going to a fancy dress party, i.e. dresses like it was that era. Thanks Mirela

Coding

Coded - Design and coding required

```html
<!DOCTYPE html>
<html lang="en">
<head>
<meta charset="utf-8">
<title>Marbled Sparrow — Vintage Clothing</title>
<link href="https://fonts.googleapis.com/css2?family=Open+Sans:ital,wght@0,400;0,600;0,700;1,600;1,700&display=swap" rel="stylesheet">
<style>
:root{
  --olive:#6a7450;
  --olive-dark:#4f5a1f;
  --sage:#cdd4a9;
  --cream:#fbfcee;
  --blush:#dfd6d6;
  --red:#d3141e;
  --ink:#2b2b2b;
  --grey-band:#e4e4e4;
  --footer-dark:#2f2f2f;
  --white:#fff;
}
*{box-sizing:border-box;margin:0;padding:0}
html,body{width:669px;height:1200px;overflow:hidden}
body{position:relative;font-family:"Open Sans",Arial,sans-serif;color:var(--ink);background:var(--white)}
.abs{position:absolute}
a{color:inherit;text-decoration:none}

/* header */
.brand{left:94px;top:20px;display:flex;align-items:center;gap:7px;font-size:21px;font-weight:600;color:var(--olive)}
.brand-dot{width:12px;height:12px;border-radius:50%;background:var(--red)}
.utility{top:8px;font-size:8.5px;color:#333;display:flex;align-items:center;gap:5px}
.utility svg{width:12px;height:12px}
.util-sep{top:4px;width:1px;height:20px;background:#999}
.search-field{left:358px;top:33px;width:104px;height:12px;border:1px solid #aaa;font-size:5px;color:#999;padding:2px 4px;font-style:italic}
.btn-green{background:var(--olive-dark);color:#fff;font-size:7px;display:flex;align-items:center;justify-content:center}

/* nav */
.nav{left:0;top:54px;width:669px;height:41px;background:var(--olive)}
.nav-link{top:71px;font-size:8.5px;color:#fff}
.ship{left:462px;top:61px;width:114px;height:20px;display:flex}
.ship-red{background:var(--red);color:#fff;font-weight:700;font-size:8.5px;width:70px;display:flex;align-items:center;justify-content:center}
.ship-dark{background:#222;color:#fff;font-size:5px;flex:1;display:flex;align-items:center;justify-content:center;text-align:center;line-height:1.2}
.ship-note{left:467px;top:82px;font-size:5px;color:#fff;font-style:italic;text-decoration:underline}

/* hero */
.hero{left:77px;top:96px;width:515px;height:298px;background:#fff;box-shadow:0 1px 3px rgba(0,0,0,.35)}
.hero-inner{left:82px;top:100px;width:505px;height:289px;background:var(--blush)}
.hero-pointer{left:124px;top:83px}
.hero-model{left:150px;top:105px;width:66px;height:273px;border-radius:30px 30px 8px 8px;background:linear-gradient(#5a2020,#a82a2e 35%,#c99 70%,#2b2222)}
.hero-title{left:250px;top:158px;width:280px;font-size:20px;font-weight:700;font-style:italic;line-height:24px;text-align:center;color:#222}
.hero-copy{left:254px;top:213px;width:270px;font-size:8px;line-height:10.5px;color:#333}
.hero-btn{left:334px;top:266px;width:61px;height:19px;border-radius:2px;font-size:9px;font-weight:600}
.dot{top:374px;width:11px;height:11px;border-radius:50%;background:#fff}

/* cream body */
.cream{left:0;top:394px;width:669px;height:559px;background:var(--cream)}
.section-title{left:93px;top:420px;font-size:16.5px;font-weight:600;color:#333}
.product{top:450px;width:108px;height:148px;background:#fff;border:1px solid #ccc;box-shadow:0 1px 2px rgba(0,0,0,.2)}
.product-img{position:absolute;left:3px;top:3px;width:100px;height:105px}
.product-cap{position:absolute;left:3px;top:108px;width:100px;height:36px;background:var(--sage);text-align:center}
.product-name{font-size:8px;color:#333;margin-top:3px}
.product-buy{font-size:9.5px;color:var(--olive-dark);margin-top:2px;display:flex;justify-content:center;align-items:center;gap:3px}
.badge{position:absolute;right:-9px;top:-9px;width:38px;height:38px;border-radius:50%;background:var(--red);border:2px solid #fff;box-shadow:0 1px 2px rgba(0,0,0,.3);color:#fff;font-size:8.5px;font-weight:600;line-height:11px;text-align:center;padding-top:7px}

.promo{top:628px;width:155px;height:217px;background:#fff;border:1px solid #ccc;box-shadow:0 1px 2px rgba(0,0,0,.2)}
.promo-body{position:absolute;left:3px;top:3px;right:3px;bottom:3px}
.tips{background:var(--sage)}
.tips-photo{position:absolute;left:4px;top:20px;width:48px;height:190px;border-radius:20px 20px 6px 6px;background:linear-gradient(#222,#c92a2a 25%,#e2b8a0 45%,#222 60%,#d9b49b 80%,#222)}
.tips-title{position:absolute;left:56px;top:4px;font-size:13px;font-weight:700;color:#111}
.tip{position:absolute;font-size:6.3px;line-height:7.6px;color:#333}
.tip b{color:var(--olive-dark);font-weight:600;display:block;font-size:7px}
.era{background:#3f3f3f}
.era-photo{position:absolute;left:0;top:0;width:47px;height:100%;background:linear-gradient(#6d6658,#a8978a 50%,#4d4038)}
.era-title{position:absolute;left:47px;right:0;top:4px;text-align:center;color:#fff;font-size:13px;font-weight:600}
.era-copy{position:absolute;left:52px;right:4px;top:28px;color:#fff;font-size:7.5px;line-height:8.7px;text-align:center}
.vip{background:radial-gradient(circle at 40% 45%,#6c6c64,#3a3a36)}
.vip-join{position:absolute;left:9px;top:18px;color:#fff;font-weight:700;font-size:10px}
.vip-name{position:absolute;left:0;right:0;top:40px;text-align:center;color:#fff;font-weight:700;font-size:22px}
.vip-offer{position:absolute;left:0;right:0;top:87px;text-align:center;color:#fff;font-weight:700;font-size:9.5px}
.vip-offer span{color:var(--red)}
.vip-copy{position:absolute;left:8px;right:8px;top:104px;text-align:center;color:#fff;font-size:7.5px;line-height:9px}

.motto{left:80px;top:868px}
.motto-text{left:92px;top:884px;width:485px;text-align:center;color:#fff;font-style:italic;font-weight:600;font-size:14.5px;line-height:18px}

/* community */
.community{left:0;top:953px;width:669px;height:95px;background:var(--grey-band)}
.community-title{left:93px;top:959px;font-size:14.5px;font-weight:400;color:#222}
.label{top:983px;font-size:11.5px;color:#222}
.email{left:93px;top:1005px;width:154px;height:19px;border:1px solid #555;background:#fff;display:flex}
.email-field{flex:1;font-size:8px;color:#888;padding:4px 6px}
.email-btn{width:54px;font-size:8px}
.social{top:1006px;width:14px;height:14px;border-radius:50%;background:#444}

/* footer */
.footer{left:0;top:1048px;width:669px;height:118px;background:var(--olive)}
.col-title{top:1050px;font-size:11.5px;font-weight:600;color:#fff}
.col-links{top:1071px;font-size:8.2px;line-height:14.4px;color:#e7e9da}
.col-rule{top:1066px;width:1px;height:85px;background:#8c946f}
.legal{left:0;top:1166px;width:669px;height:34px;background:var(--footer-dark)}
.copyright{left:102px;top:1180px;font-size:6.2px;color:#ddd;letter-spacing:.3px}
.seal{top:1177px;display:flex;align-items:center;gap:4px;color:#fff;font-size:10px;font-weight:600;white-space:nowrap}
.seal i{display:block;width:10px;height:10px;border-radius:50%;background:#e7822a}
.card{top:1178px;width:18px;height:11px;border-radius:1px}
</style>
</head>
<body>

<!-- header -->
<div class="abs brand"><span class="brand-dot"></span>Marbled Sparrow</div>
<div class="abs utility" style="left:365px"><svg viewBox="0 0 12 12"><path d="M0 2h2l2 6h6l1-4H3" fill="none" stroke="#333" stroke-width="1.2"/><circle cx="5" cy="10.5" r="1" fill="#333"/><circle cx="9" cy="10.5" r="1" fill="#333"/></svg>View Cart</div>
<div class="abs util-sep" style="left:438px"></div>
<div class="abs utility" style="left:455px"><svg viewBox="0 0 12 12"><rect x="2" y="0.5" width="8" height="11" fill="none" stroke="#333"/><path d="M4 3h4M4 5.5h4M4 8h4" stroke="#333"/></svg>Wish List</div>
<div class="abs util-sep" style="left:525px"></div>
<div class="abs utility" style="left:535px"><svg viewBox="0 0 12 12"><circle cx="6" cy="6" r="5" fill="none" stroke="#333" stroke-width="1.2"/><circle cx="6" cy="6" r="2.3" fill="none" stroke="#333"/></svg>Help</div>
<div class="abs search-field">Search one off vintage items...</div>
<div class="abs btn-green" style="left:464px;top:33px;width:29px;height:12px">search</div>
<div class="abs btn-green" style="left:510px;top:33px;width:66px;height:12px">Sign Up / Login</div>

<!-- nav -->
<nav class="abs nav"></nav>
<svg class="abs" style="left:94px;top:67px" width="14" height="13" viewBox="0 0 14 13"><path d="M7 0L0 6h2v7h4V9h2v4h4V6h2z" fill="#fff"/></svg>
<a class="abs nav-link" style="left:130px">Women</a>
<a class="abs nav-link" style="left:190px">Men</a>
<a class="abs nav-link" style="left:358px">Style Tips</a>
<a class="abs nav-link" style="left:412px">FAQs</a>
<div class="abs ship"><div class="ship-red">Free Shipping</div><div class="ship-dark">on orders<br>$100&amp;over!</div></div>
<a class="abs ship-note">Find out more about delivery &amp; shipping</a>

<!-- hero slider -->
<div class="abs hero"></div>
<div class="abs hero-inner"></div>
<svg class="abs hero-pointer" width="40" height="18" viewBox="0 0 40 18"><path d="M0 18L20 0l20 18z" fill="#fff"/></svg>
<div class="abs hero-model" role="img" aria-label="Young woman in a red vintage playsuit, black hat and ankle boots"></div>
<h1 class="abs hero-title">Check Out Our Lookbook! For all the Latest Fashion Trends</h1>
<p class="abs hero-copy">Lorem Ipsum is simply dummy text of the printing and typesetting industry. Lorem Ipsum has been the industry's standard dummy text ever since..</p>
<a class="abs btn-green hero-btn">Buy Now</a>
<span class="abs dot" style="left:312px"></span>
<span class="abs dot" style="left:328px;background:#fff;box-shadow:inset 0 0 0 3px #fff,inset 0 0 0 6px var(--olive-dark)"></span>
<span class="abs dot" style="left:344px"></span>

<!-- featured -->
<div class="abs cream"></div>
<h2 class="abs section-title">Featured Products</h2>

<div class="abs product" style="left:93px">
  <div class="product-img" role="img" aria-label="Green pleated 1950s party dress" style="background:linear-gradient(#fff,#2a9a70 30%,#1f7f5c 90%,#fff)"></div>
  <div class="product-cap"><div class="product-name">1950s Party Dress</div><div class="product-buy">Buy Now <svg width="10" height="10" viewBox="0 0 10 10"><circle cx="5" cy="5" r="4.3" fill="none" stroke="#4f5a1f" stroke-width="1.2"/><path d="M4 3l2 2-2 2" fill="none" stroke="#4f5a1f" stroke-width="1.2"/></svg></div></div>
  <div class="badge">$25<br>Only</div>
</div>
<div class="abs product" style="left:218px">
  <div class="product-img" role="img" aria-label="Woman in a brown double breasted coat" style="background:linear-gradient(#fff,#5a3a2a 30%,#2a1f1a 90%,#fff)"></div>
  <div class="product-cap"><div class="product-name">Double Breasted Coat</div><div class="product-buy">Buy Now <svg width="10" height="10" viewBox="0 0 10 10"><circle cx="5" cy="5" r="4.3" fill="none" stroke="#4f5a1f" stroke-width="1.2"/><path d="M4 3l2 2-2 2" fill="none" stroke="#4f5a1f" stroke-width="1.2"/></svg></div></div>
  <div class="badge">$30<br>Only</div>
</div>
<div class="abs product" style="left:343px">
  <div class="product-img" role="img" aria-label="Woman in a black 1960s style blouse" style="background:linear-gradient(#fff,#2a2a2a 35%,#111 90%,#fff)"></div>
  <div class="product-cap"><div class="product-name">1960s Hippy Dress</div><div class="product-buy">Buy Now <svg width="10" height="10" viewBox="0 0 10 10"><circle cx="5" cy="5" r="4.3" fill="none" stroke="#4f5a1f" stroke-width="1.2"/><path d="M4 3l2 2-2 2" fill="none" stroke="#4f5a1f" stroke-width="1.2"/></svg></div></div>
  <div class="badge">$25<br>Only</div>
</div>
<div class="abs product" style="left:468px">
  <div class="product-img" role="img" aria-label="Navy 1980s high waisted pants" style="background:linear-gradient(#fff,#243a5e 25%,#1c2e4d 85%,#fff)"></div>
  <div class="product-cap"><div class="product-name">1980s High Pant</div><div class="product-buy">Buy Now <svg width="10" height="10" viewBox="0 0 10 10"><circle cx="5" cy="5" r="4.3" fill="none" stroke="#4f5a1f" stroke-width="1.2"/><path d="M4 3l2 2-2 2" fill="none" stroke="#4f5a1f" stroke-width="1.2"/></svg></div></div>
  <div class="badge">$35<br>Only</div>
</div>

<!-- promos -->
<div class="abs promo" style="left:93px"><div class="promo-body tips">
  <div class="tips-photo" role="img" aria-label="Pin-up style woman in red top and navy shorts"></div>
  <div class="tips-title">Style Tips</div>
  <div class="tip" style="left:62px;top:23px;width:82px;text-align:center"><b>Tip1</b>Lorem ipsum dolor sit amet, consectetur adipisc- ing elit, sed do eiusmod tempor incididunt.</div>
  <div class="tip" style="left:60px;top:76px;width:84px;text-align:center"><b>Tip2</b>Lorem ipsum dolor sit amet, consectetur adipisc- ing elit, sed do eiusmod tempor.</div>
  <div class="tip" style="left:58px;top:125px;width:86px;text-align:center"><b>Tip3</b>Lorem ipsum dolor sit amet, consectetur adipisc- ing .</div>
  <div class="tip" style="left:50px;top:163px;width:96px;text-align:center"><b>Tip4</b>Lorem ipsum dolor sit amet, consectetur adipiscing elit, sed do eiusmod tempor.</div>
</div></div>
<div class="abs promo" style="left:257px"><div class="promo-body era">
  <div class="era-photo" role="img" aria-label="Vintage boutique interior with mannequins"></div>
  <div class="era-title">Shop Era</div>
  <p class="era-copy">"Lorem ipsum dolor sit amet, consectetur adipiscing elit, sed do eiusmod tempor incid- idunt ut labore et dolore magna aliqua. Ut enim ad minim veniam, quis nostrud exercitation ullamco laboris nisi ut aliquip ex ea commodo con- sequat. Duis aute irure dolor in reprehenderit in voluptate velit esse cillum dolore eu fugiat nulla pariatur.</p>
</div></div>
<div class="abs promo" style="left:422px"><div class="promo-body vip" role="img" aria-label="Champagne glasses in soft focus">
  <div class="vip-join">JOIN OUR</div>
  <div class="vip-name">VIP club</div>
  <div class="vip-offer">Receive <span>5%</span> off every order!</div>
  <p class="vip-copy">Lorem ipsum dolor sit amet, con- sectetur adipiscing elit, sed do eiusmod tempor incididunt ut labore et dolore magna aliqua.</p>
</div></div>

<!-- motto -->
<svg class="abs motto" width="509" height="74" viewBox="0 0 509 74">
  <path fill="var(--olive)" d="M8 0 L501 0 L509 5 L501 10 L509 15 L501 20 L509 25 L501 30 L509 35 L501 40 L509 45 L501 50 L509 55 L501 60 L509 65 L501 70 L501 74 L8 74 L8 70 L0 65 L8 60 L0 55 L8 50 L0 45 L8 40 L0 35 L8 30 L0 25 L8 20 L0 15 L8 10 L0 5 Z"/>
</svg>
<p class="abs motto-text">Marbled Sparrow is all about being different. That’s way all of our clothes are unique</p>

<!-- community -->
<div class="abs community"></div>
<h2 class="abs community-title">Become part of our community</h2>
<div class="abs label" style="left:93px">Sign up to our newsletter:</div>
<div class="abs email"><div class="email-field">Enter your Email</div><div class="btn-green email-btn">SUBSCRIBE</div></div>
<div class="abs label" style="left:422px">follow us in social media:</div>
<span class="abs social" style="left:424px" aria-label="Social network"></span>
<span class="abs social" style="left:441px" aria-label="Social network"></span>
<span class="abs social" style="left:458px" aria-label="Social network"></span>
<span class="abs social" style="left:475px" aria-label="Social network"></span>
<span class="abs social" style="left:492px" aria-label="Social network"></span>

<!-- footer -->
<footer class="abs footer"></footer>
<div class="abs col-title" style="left:116px">Marbled Sparrow</div>
<div class="abs col-links" style="left:116px">About us<br>Terms of use<br>Privacy policy<br>Press</div>
<div class="abs col-rule" style="left:246px"></div>
<div class="abs col-title" style="left:287px">Connect with Us</div>
<div class="abs col-links" style="left:298px;line-height:12.9px">Contact us<br>My Account<br>Style Tips<br>FAQs<br>Shipping<br>Track your order<br>Size chart</div>
<div class="abs col-rule" style="left:401px"></div>
<div class="abs col-title" style="left:423px">Shop by Popular Categories</div>
<div class="abs col-links" style="left:472px">Men<br>Women<br>Accessories<br>Bages<br>Shoes</div>
<div class="abs col-links" style="left:539px">50s<br>60s<br>70s<br>80s<br>90s</div>

<div class="abs legal"></div>
<div class="abs copyright">Copyright © Marbled Sparrow. All Prices are in AUD.</div>
<div class="abs seal" style="left:318px"><i></i>Keystone Seal</div>
<div class="abs seal" style="left:414px">Payroute</div>
<span class="abs card" style="left:470px;background:#2e77bb"></span>
<span class="abs card" style="left:490px;background:#fff"></span>
<span class="abs card" style="left:510px;background:#1a4fa0"></span>
<span class="abs card" style="left:530px;background:#e9a23b"></span>
<span class="abs card" style="left:550px;background:#fff"></span>

</body>
</html>
```